Demo, Strip out Rubbish and Asbestos Removal

we need a business card to give to clients to provide information about our Demo Strip out rubbish and Asbestos removal as well as labour hire.
I was thinking of a silhouette of a tip truck with the services we provide being dumped out the back in bullet form.
KB in a green colour and Refuse in a grey colour.
Greens, greys, blacks, white, silvers, matt grey. But am very open to other colour schemers and designs. I do like the tough of a matt card with gloss writing or vies versa.
We are also looking to use this design as our logo

Target Market(s)

builders - commercial residential . General public

Industry/Entity Type

Business

Contact Information for Business Card

KB Refuse
Dean Harlow
0471203658
kbrefuse@mailvista.example

Font styles to use
Sans Serif

Colors
9bcb3c
00a990
0355a3
000000
5c5c5c
cbcbcb
fbee3f
ffffff
ffcf3e

Requirements
Must have
• Abn: 57219038446
Nice to have
• bullet form
:demo and strip out
:asbestos and rubbishe removal
:labour hire
:Residential and commercial clean up
:yard clearing

```html
<!DOCTYPE html>
<html lang="en">
<head>
<meta charset="utf-8">
<title>KB Refuse — Business Cards</title>
<link rel="stylesheet" href="https://fonts.googleapis.com/css2?family=Jost:wght@400&display=swap">
<style>
  :root {
    --backdrop: #e2c9a2;
    --card-top: #3d3f3f;
    --card-bottom: #070707;
    --text-light: #e4e4e4;
    --brand-green: #9cb4a2;
    --texture-light: #5a5d5c;
    --texture-dark: #262827;
  }
  * { margin: 0; padding: 0; box-sizing: border-box; }
  html, body {
    width: 900px; height: 1200px; overflow: hidden;
    background: var(--backdrop);
  }
  .canvas { position: relative; width: 900px; height: 1200px; }
  .card {
    position: absolute; width: 770px; height: 428px;
    border-radius: 8px; overflow: hidden;
    font-family: "Jost", Arial, sans-serif;
    font-weight: 400;
    color: var(--text-light);
    box-shadow: 0 3px 8px rgba(0,0,0,0.35);
  }
  .card--front {
    left: 82px; top: 65px;
    background: linear-gradient(180deg, var(--card-top) 0%, #1c1d1d 55%, var(--card-bottom) 100%);
  }
  .card--back {
    left: 38px; top: 698px; height: 430px;
    background: linear-gradient(110deg, #303131 0%, #141414 45%, var(--card-bottom) 100%);
  }
  .texture { position: absolute; inset: 0; width: 100%; height: 100%; }
  .brand {
    position: absolute; display: flex; align-items: center;
    color: var(--brand-green); text-transform: uppercase; white-space: nowrap;
    line-height: 1;
  }
  .brand__mark { background: var(--brand-green); display: inline-block; flex: none; }
  .name { position: absolute; white-space: nowrap; letter-spacing: 0.3em; line-height: 1; }
  .contact { position: absolute; white-space: nowrap; letter-spacing: 0.12em; line-height: 1.4; }

  .card--front .brand { left: 43px; top: 84px; font-size: 52px; letter-spacing: 0.05em; gap: 14px; }
  .card--front .brand__mark { width: 36px; height: 36px; }
  .card--front .name { left: 43px; top: 166px; font-size: 32px; }
  .card--front .contact { left: 43px; top: 234px; font-size: 21px; }

  .card--back .brand { left: 0; right: 0; justify-content: center; top: 148px; font-size: 68px; letter-spacing: 0.05em; gap: 18px; }
  .card--back .brand__mark { width: 46px; height: 46px; }
  .card--back .name,
  .card--back .contact { left: 0; right: 0; text-align: center; }
  .card--back .name { top: 238px; font-size: 30px; }
  .card--back .contact { top: 298px; font-size: 20px; }
</style>
</head>
<body>
<main class="canvas">
  <section class="card card--front">
    <svg class="texture" viewBox="0 0 770 428" role="img" aria-label="Embossed tyre-track texture running diagonally across the card">
      <defs>
        <linearGradient id="trackFront" x1="0" y1="0" x2="1" y2="1">
          <stop offset="0" stop-color="#5a5d5c" stop-opacity="0.7"/>
          <stop offset="0.6" stop-color="#262827" stop-opacity="0.8"/>
          <stop offset="1" stop-color="#1a1a1a" stop-opacity="0.6"/>
        </linearGradient>
      </defs>
      <path d="M150 0 L330 0 Q520 80 650 210 Q730 300 770 330 L770 428 L700 428 Q640 340 540 260 Q400 150 260 80 Q190 40 150 0 Z" fill="url(#trackFront)"/>
    </svg>
    <div class="brand"><span class="brand__mark"></span>KB Refuse</div>
    <div class="name">Dean Harlow</div>
    <div class="contact">T: 0471203658<br>E: kbrefuse@mailvista.example<br>ABN: 57219038446</div>
  </section>

  <section class="card card--back">
    <svg class="texture" viewBox="0 0 770 430" role="img" aria-label="Faint embossed tyre-track texture in the upper left corner">
      <defs>
        <linearGradient id="trackBack" x1="0" y1="0" x2="1" y2="1">
          <stop offset="0" stop-color="#5a5d5c" stop-opacity="0.55"/>
          <stop offset="1" stop-color="#262827" stop-opacity="0"/>
        </linearGradient>
      </defs>
      <path d="M0 0 L90 0 Q200 90 270 190 Q300 250 250 300 Q170 240 80 200 Q30 180 0 170 Z" fill="url(#trackBack)"/>
    </svg>
    <div class="brand"><span class="brand__mark"></span>KB Refuse</div>
    <div class="name">Dean Harlow</div>
    <div class="contact">T: 0471203658<br>E: kbrefuse@mailvista.example<br>ABN: 57219038446</div>
  </section>
</main>
</body>
</html>
```